Need Poster Design for Indie Family Film

We need a poster for a indie family film and would like to see designs that should be elegant, bold and playful.

Maribel follows the parallel stories of three Singaporeans dealing with familial love and loss: a young girl copes with her mother’s death by living in an imaginary world, a father struggles to reconcile with his estranged daughter before her wedding and a woman fails to convince her family of her desire to become a singer. Staring Darlene Pruitt, Mirabel Tan with veterans Rosnah Yusof, Farid Osmani and Derek Lam and Calvin Teo

Target Market(s)

7-14 and Parents

Number of Pages Required

3 page

Font styles to use
Serif

Requirements
Must have
• Film Title: Maribel
Nice to have
• The poster doesn't have to incorporate the photos and can use other design elements like illustrations.
Should not have
• Anything offensive and disturbing.

```html
<!DOCTYPE html>
<html lang="en">
<head>
<meta charset="utf-8">
<title>Maribel — Film Poster</title>
<link rel="stylesheet" href="https://fonts.googleapis.com/css2?family=Sorts+Mill+Goudy&family=Lato:wght@300;700&display=swap">
<style>
  :root {
    --canvas-bg: #e9e6e1;
    --poster-maroon: #5c1416;
    --accent-gold: #f8bf4a;
    --credit-grey: #b79a93;
  }
  * { margin: 0; padding: 0; box-sizing: border-box; }
  html, body {
    width: 1200px; height: 900px; overflow: hidden;
    background: var(--canvas-bg);
  }
  .poster {
    position: absolute; left: 314px; top: 20px;
    width: 572px; height: 860px;
    background: var(--poster-maroon);
    overflow: hidden;
    font-family: "Lato", sans-serif;
  }
  .artwork { position: absolute; background: var(--accent-gold); }
  .artwork--reaching-hand { left: 264px; top: 0; width: 179px; height: 229px; border-radius: 0 0 60px 60px; }
  .artwork--rising-hand { left: 302px; top: 376px; width: 201px; height: 484px; border-radius: 70px 70px 0 0; }
  .film-title {
    position: absolute; left: 100px; width: 450px; top: 226px;
    text-align: center;
    font-family: "Sorts Mill Goudy", serif;
    font-size: 100px; line-height: 1;
    color: var(--accent-gold);
  }
  .film-facts {
    position: absolute; top: 320px;
    font-size: 11px; font-weight: 700; color: var(--accent-gold);
    white-space: nowrap;
  }
  .film-facts--release { left: 145px; }
  .film-facts--genre { left: 297px; }
  .film-directors {
    position: absolute; left: 297px; top: 335px;
    font-size: 7px; font-weight: 700; color: var(--accent-gold);
    white-space: nowrap;
  }
  .credits {
    position: absolute; right: 292px; top: 364px;
    text-align: right; list-style: none;
  }
  .credit { height: 30.4px; }
  .credit__role { display: block; font-size: 8px; font-weight: 700; color: #ffffff; line-height: 11px; }
  .credit__name { display: block; font-size: 8px; font-weight: 300; color: var(--credit-grey); line-height: 12px; }
  .synopsis {
    position: absolute; left: 90px; top: 767px; width: 190px;
    text-align: right;
    font-size: 5.6px; line-height: 6.8px; font-weight: 300;
    color: var(--credit-grey);
  }
</style>
</head>
<body>
  <main class="poster">
    <div class="artwork artwork--reaching-hand" role="img" aria-label="Illustrated golden hand reaching down from the top edge"></div>

    <h1 class="film-title">Maribel</h1>
    <p class="film-facts film-facts--release">Maribel / 2015 / 70 mins /</p>
    <p class="film-facts film-facts--genre">Drama /Singapore</p>
    <p class="film-directors">Dir. Joanne Lim, Hafiz Rahman and Marcus Lee</p>

    <ul class="credits">
      <li class="credit"><span class="credit__role">Cast:</span><span class="credit__name">Rosnah Yusof, Farid Osmani Derek Lam, Mirabel Tan, Darlene Pruitt</span></li>
      <li class="credit"><span class="credit__role">Producer:</span><span class="credit__name">Marcus Lee</span></li>
      <li class="credit"><span class="credit__role">Co Directors:</span><span class="credit__name">Hafiz Rahman and Joanne Lim/Marcus Lee</span></li>
      <li class="credit"><span class="credit__role">Director of Photography:</span><span class="credit__name">Victor Chua</span></li>
      <li class="credit"><span class="credit__role">Camera Assistant:</span><span class="credit__name">Nadia Rosli</span></li>
      <li class="credit"><span class="credit__role">Sound:</span><span class="credit__name">Amira Salleh</span></li>
      <li class="credit"><span class="credit__role">Editor:</span><span class="credit__name">Peter Alan Hargrove</span></li>
      <li class="credit"><span class="credit__role">Production Designer:</span><span class="credit__name">Wendy Goh</span></li>
      <li class="credit"><span class="credit__role">Production Art Assistant:</span><span class="credit__name">Rizal Hakim &amp; Calvin Teo</span></li>
      <li class="credit"><span class="credit__role">Music Composer:</span><span class="credit__name">Wu Lian and Ong Kai Wen</span></li>
      <li class="credit"><span class="credit__role">Production Assistant:</span><span class="credit__name">Sofia Ismail</span></li>
      <li class="credit"><span class="credit__role">Assistant Producer:</span><span class="credit__name">Lee Hui Min</span></li>
      <li class="credit"><span class="credit__role">Production Company:</span><span class="credit__name">Lumen Pictures</span></li>
    </ul>

    <p class="synopsis">Maribel follows the parallel stories of three Singaporeans dealing with familial love and loss: a young girl copes with her mother's death by living in an imaginary world, a father struggles to reconcile with his estranged daughter before her wedding and a woman fails to convince her family of her desire to become a singer. Starring Darlene Pruitt, Mirabel Tan with veterans Rosnah Yusof, Farid Osmani and Derek Lam.</p>

    <div class="artwork artwork--rising-hand" role="img" aria-label="Illustrated golden hand rising up from the bottom edge"></div>
  </main>
</body>
</html>
```